" A empresa está localizada numa cidade pequena, porém muito próximos da capital do estado de Minas Gerais e de outras cidades maiores do interior. Considerada região metropolitana da capital. Criaremos um site e faremos venda de produtos na loja virtual, bem como marcação de serviços. Queremos trazer profissionalismo e um serviço diferenciado para a região. Nossa meta é em 3 anos ser a principal referência nesse serviço num raio de 50 km da cidade. "

```html
<!DOCTYPE html>
<html lang="pt-BR">
<head>
<meta charset="UTF-8">
<title>Folha Clara – Pasta</title>
<link href="https://fonts.googleapis.com/css2?family=Cinzel:wght@500&family=Open+Sans:wght@400;600&display=swap" rel="stylesheet">
<style>
  :root {
    --teal: #78aaa6;
    --teal-dark: #5f918d;
    --paper: #ffffff;
    --backdrop: #e9e9e9;
    --gold: #c9a85a;
    --gold-light: #ecd9a0;
    --ink: #3d3d3d;
    --ink-soft: #6b6b6b;
    --ghost: #f0f0f0;
  }
  * { margin: 0; padding: 0; box-sizing: border-box; }
  html, body { width: 1200px; height: 1200px; overflow: hidden; }
  body { background: var(--backdrop); font-family: "Open Sans", sans-serif; position: relative; }

  .folder { position: absolute; left: 110px; top: 158px; width: 1008px; height: 658px; display: flex; }
  .folder__inside { position: relative; width: 502px; height: 100%; background: var(--paper); }
  .folder__cover { position: relative; flex: 1; height: 100%; background: var(--teal); }
  .edge { position: absolute; top: 0; width: 9px; height: 100%;
          background: linear-gradient(90deg, var(--gold), var(--gold-light), var(--gold)); }
  .edge--left { left: 0; }
  .edge--right { right: 0; }

  .ghost-mark { position: absolute; left: 120px; top: 6px; width: 300px; height: 300px;
                border-radius: 50%; background: var(--ghost); }

  .contacts { position: absolute; left: 30px; bottom: 16px; list-style: none; }
  .contacts li { display: flex; align-items: center; gap: 9px; font-size: 11px;
                 color: var(--ink-soft); line-height: 1.25; margin-top: 11px; }
  .contacts svg { flex: none; width: 16px; height: 16px; }

  .brand { position: absolute; left: 50%; top: 230px; transform: translateX(-50%);
           text-align: center; width: 400px; }
  .brand__dot { width: 90px; height: 90px; border-radius: 50%; background: var(--ink);
                margin: 0 auto 22px; }
  .brand__name { font-family: "Cinzel", serif; font-weight: 500; font-size: 46px;
                 color: var(--ink); letter-spacing: 1px; line-height: 1; }
  .brand__tagline { font-family: "Cinzel", serif; font-weight: 500; font-size: 19px;
                    color: var(--ink); letter-spacing: 1px; margin-top: 4px; }

  .pocket { position: absolute; left: 110px; top: 816px; width: 500px; height: 220px; }
</style>
</head>
<body>
  <main class="folder">
    <section class="folder__inside">
      <div class="edge edge--left"></div>
      <div class="ghost-mark"></div>
      <ul class="contacts">
        <li><svg viewBox="0 0 16 16"><circle cx="8" cy="8" r="8" fill="#6b6b6b"/><path d="M5.5 4.5l1.5 0 .6 2-.9.7a5 5 0 0 0 2.1 2.1l.7-.9 2 .6v1.5c-3.5.3-6.3-2.5-6-6z" fill="#fff"/></svg>(31) 9 9000-1234</li>
        <li><svg viewBox="0 0 16 16"><circle cx="8" cy="8" r="8" fill="#6b6b6b"/><rect x="4" y="5" width="8" height="6" fill="none" stroke="#fff"/><path d="M4 5l4 3 4-3" fill="none" stroke="#fff"/></svg>contato@folhaclara.net</li>
        <li><svg viewBox="0 0 16 16"><circle cx="8" cy="8" r="8" fill="#6b6b6b"/><circle cx="8" cy="8" r="4" fill="none" stroke="#fff"/><path d="M4 8h8M8 4c-2 2.5-2 5.5 0 8M8 4c2 2.5 2 5.5 0 8" fill="none" stroke="#fff" stroke-width=".8"/></svg>www.folhaclara.net.br</li>
        <li><svg viewBox="0 0 16 16"><circle cx="8" cy="8" r="8" fill="#6b6b6b"/><path d="M8 13s-3.5-3.8-3.5-6a3.5 3.5 0 0 1 7 0c0 2.2-3.5 6-3.5 6z" fill="#fff"/><circle cx="8" cy="7" r="1.2" fill="#6b6b6b"/></svg><span>Rua das Acácias, 120.<br>Centro - MG</span></li>
        <li><svg viewBox="0 0 16 16"><circle cx="8" cy="8" r="8" fill="#6b6b6b"/></svg>folhaclara.net</li>
        <li><svg viewBox="0 0 16 16"><circle cx="8" cy="8" r="8" fill="#6b6b6b"/></svg>@folhaclara18</li>
      </ul>
    </section>
    <section class="folder__cover">
      <div class="edge edge--right"></div>
      <div class="brand">
        <div class="brand__dot"></div>
        <div class="brand__name">FOLHA CLARA</div>
        <div class="brand__tagline">PORQUE VOCÊ É ÚNICA</div>
      </div>
    </section>
  </main>
  <svg class="pocket" viewBox="0 0 500 220" aria-hidden="true">
    <path d="M0 0H500V0C500 0 470 40 470 90C470 170 380 215 230 218C160 219 70 214 0 208Z" fill="var(--teal)"/>
    <path d="M0 0H500" stroke="var(--teal-dark)" stroke-width="1"/>
  </svg>
</body>
</html>
```